Bright Towns Alliance PowerPoint Design Template and Sample Deck

The Bright Towns Alliance is an international organization that seeks to improve the livability, workability and sustainability of the world’s cities.
We seek a versatile PowerPoint design template with 10 slide types plus a “self-documenting” sample deck. Your design will be used in keynote speeches and workshops around the world.
After the contest is completed, we will ask the winning designer to add 10-20 additional slide types for $75 per slide. We also seek a long-term relationship whereby we can request “custom” slides and/or ask the designer to touch up the slides we build to make them better.
FILES. We have uploaded several files:
1. BRIGHT TOWNS ALLIANCE DESIGN CONTEST NOTES.docx with full instructions.
2. PALETTE. Shows our official colors.
3 LOGOS. Several individual files with different variations of our logo. Some with our motto, some without.
2. SAMPLE SLIDES. Because we were unable to successfully upload our sample deck, we are making it available via this FileCrate link:
https://www.filecrate-example.net/s/k7qvmr2tn8wzd4h/The%20Bright%20Towns%20Alliance%20Design%20Contest%20Notes.docx?dl=0
Target Market(s)
Mayors, department heads, CIOs, senior executives from technology companies
Industry/Entity Type
Information Technology
Colors
Designer to choose colors to be used in the design.
Requirements
Must have
- Please see uploaded Word document for requirements, nice to haves and should not haves and uploaded palette for color preferences.
Nice to have
- see above
Should not have
- see above

```html
<!DOCTYPE html>
<html lang="en">
<head>
<meta charset="utf-8">
<title>Bright Towns Alliance – PowerPoint Template Deck</title>
<link href="https://fonts.googleapis.com/css2?family=Open+Sans:wght@400;600;700;800&display=swap" rel="stylesheet">
<style>
:root{
  --navy:#1c2f5c;
  --navy-dark:#142246;
  --orange:#f4a321;
  --ink:#2b2f38;
  --grey:#8a8f99;
  --line:#d7dae0;
  --paper:#ffffff;
  --canvas:#eef0f3;
  --soft:#f5f6f8;
}
*{box-sizing:border-box;margin:0;padding:0}
html,body{width:891px;height:1200px;overflow:hidden;background:var(--canvas);font-family:"Open Sans",Arial,sans-serif;color:var(--ink)}
.deck{width:891px;height:1200px;padding:9px 8px;display:grid;grid-template-columns:repeat(3,1fr);grid-template-rows:repeat(7,1fr);gap:9px}
.slide{position:relative;overflow:hidden;background:var(--paper);box-shadow:0 0 0 1px #dde0e5}

/* photo placeholders */
.photo{position:absolute}
.ph-city{background:linear-gradient(180deg,#4b6d96 0%,#2e4a72 55%,#1f3456 100%)}
.ph-person{background:linear-gradient(135deg,#c9ccd1 0%,#8c95a3 60%,#4d5a70 100%)}
.ph-elder{background:linear-gradient(135deg,#6d6560 0%,#3b3834 100%)}
.ph-street{background:linear-gradient(160deg,#c6a27a 0%,#8a7b6b 50%,#5a6475 100%)}
.ph-coast{background:linear-gradient(180deg,#9fb6c9 0%,#b38a68 60%,#7a6a58 100%)}
.ph-tram{background:linear-gradient(180deg,#a8b8c8 0%,#d49a4e 55%,#6c6259 100%)}
.ph-night{background:linear-gradient(180deg,#2d4a78 0%,#1b2d52 70%,#0f1a33 100%)}

/* brand lockup */
.brand{display:flex;align-items:center;gap:3px;font-weight:700;color:var(--navy);white-space:nowrap}
.brand .dot{width:5px;height:5px;border-radius:50%;background:var(--orange)}
.brand.light{color:#fff}

/* common text */
.h-slide{font-size:7.5px;font-weight:700;color:var(--navy);text-align:center}
.rule{width:22px;height:2px;background:var(--orange);margin:3px auto 0}
.txt{font-size:3.6px;line-height:1.45;color:var(--grey)}
.foot{position:absolute;left:0;right:0;bottom:0;height:9px;display:flex;align-items:center;justify-content:space-between;padding:0 6px;border-top:1px solid var(--line)}
.foot .brand{font-size:3.6px}
.foot .num{font-size:3.6px;color:#fff;background:var(--orange);padding:0 3px;height:6px;line-height:6px}
.band-head{position:absolute;top:0;left:0;right:0;height:16px;background:var(--navy);color:#fff;font-size:6px;font-weight:700;display:flex;align-items:center;padding-left:8px}
.band-head::after{content:"";position:absolute;left:0;bottom:-2px;width:40px;height:2px;background:var(--orange)}

/* title slides */
.title-card{position:absolute;left:0;right:0;top:58px;height:52px;background:#fff;text-align:center;padding-top:8px}
.title-card .brand{justify-content:center;font-size:6.5px}
.title-card h1{font-size:10px;font-weight:800;color:var(--navy);margin-top:4px;letter-spacing:.3px}
.title-card p{font-size:4.2px;color:var(--grey);margin-top:2px}
.title-card::before{content:"";position:absolute;left:0;top:0;width:60px;height:3px;background:var(--orange)}
.title-card::after{content:"";position:absolute;right:0;bottom:0;width:60px;height:3px;background:var(--orange)}
.title-base{position:absolute;left:0;right:0;bottom:0;height:51px;background:var(--navy)}
.center-card{position:absolute;left:68px;right:68px;top:50px;height:60px;background:#fff;text-align:center;padding-top:11px;border-bottom:3px solid var(--orange)}
.center-card .brand{justify-content:center;font-size:6px}
.center-card h1{font-size:9px;font-weight:800;color:var(--navy);margin-top:5px}
.center-card p{font-size:4px;color:var(--grey);margin-top:2px}

/* agenda list */
.agenda-grid{position:absolute;left:14px;right:14px;top:30px;display:grid;grid-template-columns:1fr 1fr;gap:10px 14px}
.ag-item{display:flex;gap:5px;align-items:flex-start}
.ag-num{width:14px;height:14px;background:var(--navy);color:#fff;font-size:5.5px;font-weight:700;display:flex;align-items:center;justify-content:center;flex:none;border-bottom:2px solid var(--orange)}
.ag-item b{display:block;font-size:4.6px;color:var(--navy)}
.agenda-block{position:absolute;left:0;top:0;bottom:0;width:112px;background:var(--navy);display:flex;flex-direction:column;align-items:center;justify-content:center;gap:6px}
.agenda-block span{color:#fff;font-weight:800;font-size:13px;letter-spacing:1px}
.agenda-list{position:absolute;left:124px;right:12px;top:18px;list-style:none}
.agenda-list li{display:flex;align-items:center;gap:5px;height:18px;border-bottom:1px solid var(--line);font-size:4.6px;color:var(--ink)}
.agenda-list li::before{content:"";width:7px;height:7px;background:var(--orange);flex:none}

/* quote panels */
.quote-panel{position:absolute;top:0;bottom:0;right:0;padding:22px 12px 0}
.qmark{font-size:20px;font-weight:800;line-height:1;color:var(--orange)}
.quote-panel h3{font-size:6px;font-weight:700;margin:3px 0 4px}
.btn{display:inline-block;margin-top:6px;background:var(--navy);color:#fff;font-size:4px;padding:2px 6px}

/* numbered rows */
.num-list{position:absolute;display:flex;flex-direction:column;gap:7px}
.num-row{display:flex;gap:5px;align-items:flex-start}
.num-row .n{width:13px;height:13px;background:var(--orange);color:#fff;font-size:5px;font-weight:700;display:flex;align-items:center;justify-content:center;flex:none}
.num-row b{display:block;font-size:4.6px;color:var(--navy)}

/* timeline */
.timeline{position:absolute;left:12px;right:12px;top:56px;height:50px}
.timeline .axis{position:absolute;left:0;right:0;top:10px;height:2px;background:var(--line)}
.timeline .axis i{position:absolute;left:0;top:0;height:2px;background:var(--orange)}
.stops{position:absolute;left:0;right:0;top:0;display:flex;justify-content:space-between}
.stop{width:42px;text-align:center}
.stop .c{width:20px;height:20px;border-radius:50%;margin:0 auto;background:#fff;border:2px solid var(--navy);font-size:5px;font-weight:700;color:var(--navy);display:flex;align-items:center;justify-content:center}
.stop.on .c{background:var(--orange);border-color:var(--orange);color:#fff}
.stop b{display:block;font-size:4.4px;color:var(--navy);margin-top:4px}

/* columns with photos */
.cols{position:absolute;left:10px;right:10px;top:24px;display:grid;gap:8px}
.cols .col{position:relative}
.cols .pic{position:relative;height:58px}
.cols b{display:block;font-size:4.8px;color:var(--navy);margin:4px 0 2px}
.card-or{background:var(--orange);padding:4px;margin-top:-6px;position:relative;width:86%}
.card-or b,.card-or .txt{color:#fff;margin:0}

/* process */
.process{position:absolute;left:10px;right:10px;top:44px;display:flex}
.chev{flex:1;height:22px;background:var(--navy);color:#fff;font-size:5px;font-weight:700;display:flex;align-items:center;justify-content:center;clip-path:polygon(0 0,88% 0,100% 50%,88% 100%,0 100%,12% 50%);margin-right:-4px}
.chev.alt{background:var(--orange)}
.proc-text{position:absolute;left:10px;right:10px;top:74px;display:flex;gap:6px}
.proc-text div{flex:1}
.proc-text b{display:block;font-size:4.6px;color:var(--navy);margin-bottom:2px}

/* table */
.data-table{position:absolute;left:10px;right:10px;top:24px;border-collapse:collapse;width:calc(100% - 20px);font-size:4.4px}
.data-table th{background:var(--orange);color:#fff;font-weight:700;padding:3px;text-align:left}
.data-table td{padding:3px;border-bottom:1px solid var(--line);color:var(--ink)}
.data-table tr:nth-child(even) td{background:var(--soft)}

/* contact */
.contact-shade{position:absolute;inset:0;background:rgba(20,34,70,.72)}
.contact-left{position:absolute;left:14px;top:52px;color:#fff}
.contact-left .brand{font-size:6px}
.contact-left h2{font-size:15px;font-weight:800;margin-top:4px;letter-spacing:.5px}
.contact-left h2::after{content:"";display:block;width:26px;height:2px;background:var(--orange);margin-top:4px}
.contact-list{position:absolute;right:14px;top:36px;list-style:none;display:flex;flex-direction:column;gap:8px}
.contact-list li{display:flex;align-items:center;gap:5px;font-size:4.6px;color:#fff}
.contact-list .ic{width:13px;height:13px;border-radius:50%;background:var(--orange);display:flex;align-items:center;justify-content:center;flex:none}
</style>
</head>
<body>
<main class="deck">

  <!-- Row 1: title slides -->
  <section class="slide">
    <div class="photo ph-city" role="img" aria-label="City skyline photograph" style="left:0;right:0;top:0;height:58px"></div>
    <div class="title-card">
      <div class="brand"><span class="dot"></span>Bright Towns Alliance</div>
      <h1>POWERPOINT TITLE</h1>
      <p>Subtitle goes here</p>
    </div>
    <div class="title-base photo ph-city" role="img" aria-label="City skyline photograph" style="top:110px;height:auto"></div>
  </section>

  <section class="slide">
    <div class="photo ph-city" role="img" aria-label="Aerial city photograph" style="inset:0"></div>
    <div class="center-card">
      <div class="brand"><span class="dot"></span>Bright Towns Alliance</div>
      <h1>POWERPOINT TITLE</h1>
      <p>Subtitle goes here</p>
    </div>
  </section>

  <section class="slide">
    <div class="photo ph-city" role="img" aria-label="City skyline photograph" style="left:0;right:0;top:0;height:58px"></div>
    <div class="title-card">
      <div class="brand"><span class="dot"></span>Bright Towns Alliance</div>
      <h1>POWERPOINT TITLE</h1>
      <p>Subtitle goes here</p>
    </div>
    <div class="title-base photo ph-night" role="img" aria-label="City at dusk photograph" style="top:110px;height:auto"></div>
  </section>

  <!-- Row 2: agenda -->
  <section class="slide">
    <div style="padding-top:9px"><div class="h-slide">Our Agenda</div><div class="rule"></div></div>
    <div class="agenda-grid">
      <div class="ag-item"><span class="ag-num">01</span><div><b>Topic One</b><p class="txt">Short line about the point.</p></div></div>
      <div class="ag-item"><span class="ag-num">02</span><div><b>Topic Two</b><p class="txt">Short line about the point.</p></div></div>
      <div class="ag-item"><span class="ag-num">03</span><div><b>Topic Three</b><p class="txt">Short line about the point.</p></div></div>
      <div class="ag-item"><span class="ag-num">04</span><div><b>Topic Four</b><p class="txt">Short line about the point.</p></div></div>
      <div class="ag-item"><span class="ag-num">05</span><div><b>Topic Five</b><p class="txt">Short line about the point.</p></div></div>
      <div class="ag-item"><span class="ag-num">06</span><div><b>Topic Six</b><p class="txt">Short line about the point.</p></div></div>
    </div>
    <div class="foot"><span class="brand"><span class="dot"></span>Bright Towns Alliance</span><span class="num">2</span></div>
  </section>

  <section class="slide">
    <div class="agenda-block">
      <svg width="26" height="24" viewBox="0 0 26 24" aria-hidden="true"><rect x="1.5" y="4" width="23" height="18.5" rx="2" fill="none" stroke="#fff" stroke-width="2"/><rect x="1.5" y="4" width="23" height="5" fill="#fff"/><rect x="6" y="1" width="2.5" height="6" fill="#f4a321"/><rect x="17.5" y="1" width="2.5" height="6" fill="#f4a321"/><rect x="6" y="12" width="3" height="3" fill="#fff"/><rect x="11.5" y="12" width="3" height="3" fill="#fff"/><rect x="17" y="12" width="3" height="3" fill="#f4a321"/><rect x="6" y="17" width="3" height="3" fill="#fff"/><rect x="11.5" y="17" width="3" height="3" fill="#fff"/></svg>
      <span>AGENDA</span>
    </div>
    <ul class="agenda-list">
      <li>Opening remarks and welcome</li>
      <li>Livability in growing cities</li>
      <li>Workability and data networks</li>
      <li>Sustainability targets</li>
      <li>Case studies from members</li>
      <li>Questions and next steps</li>
    </ul>
  </section>

  <section class="slide">
    <div class="band-head">Bright Towns Alliance PowerPoint Template</div>
    <div class="photo ph-coast" role="img" aria-label="Harbour city panorama photograph" style="left:10px;right:10px;top:24px;height:74px"></div>
    <p class="txt" style="position:absolute;left:10px;right:10px;top:104px">Write a short summary of the topic here. Keep the copy brief so the slide stays clear and easy to read from the back of the room during a keynote.</p>
    <div class="foot"><span class="brand"><span class="dot"></span>Bright Towns Alliance</span><span class="num">3</span></div>
  </section>

  <!-- Row 3: quotes and people -->
  <section class="slide">
    <div class="photo ph-person" role="img" aria-label="Portrait photograph of a speaker in a suit" style="left:0;top:0;bottom:0;width:46%"></div>
    <div class="quote-panel" style="left:46%">
      <div class="qmark">“</div>
      <h3 style="color:var(--navy)">Speaker Name</h3>
      <p class="txt">Add a short quote from the speaker here to support the talk.</p>
      <span class="btn">Read More</span>
    </div>
  </section>

  <section class="slide">
    <div class="photo ph-elder" role="img" aria-label="Portrait photograph of a senior executive" style="inset:0"></div>
  </section>

  <section class="slide">
    <div class="photo ph-street" role="img" aria-label="Photograph of a person in an autumn city street" style="left:0;top:0;bottom:0;width:52%"></div>
    <div class="quote-panel" style="left:52%;background:var(--navy)">
      <div class="qmark">“</div>
      <h3 style="color:#fff">Speaker Name</h3>
      <p class="txt" style="color:#c9d0de">Add a short quote from the speaker here to support the talk.</p>
    </div>
  </section>

  <!-- Row 4 -->
  <section class="slide">
    <h2 style="position:absolute;left:12px;top:38px;width:104px;font-size:8px;font-weight:800;color:var(--navy);line-height:1.25">Write Something About Your Title or Topic Here</h2>
    <div style="position:absolute;left:12px;top:80px;width:20px;height:2px;background:var(--orange)"></div>
    <div class="num-list" style="left:136px;right:12px;top:22px">
      <div class="num-row"><span class="n">01</span><div><b>First Point</b><p class="txt">A brief line of supporting text.</p></div></div>
      <div class="num-row"><span class="n">02</span><div><b>Second Point</b><p class="txt">A brief line of supporting text.</p></div></div>
      <div class="num-row"><span class="n">03</span><div><b>Third Point</b><p class="txt">A brief line of supporting text.</p></div></div>
    </div>
    <div class="foot"><span class="brand"><span class="dot"></span>Bright Towns Alliance</span><span class="num">4</span></div>
  </section>

  <section class="slide">
    <div class="num-list" style="left:12px;width:120px;top:20px">
      <div class="num-row"><span class="n">01</span><div><b>First Point</b><p class="txt">A brief line of supporting text.</p></div></div>
      <div class="num-row"><span class="n">02</span><div><b>Second Point</b><p class="txt">A brief line of supporting text.</p></div></div>
      <div class="num-row"><span class="n">03</span><div><b>Third Point</b><p class="txt">A brief line of supporting text.</p></div></div>
    </div>
    <div class="photo ph-coast" role="img" aria-label="Photograph of a hillside city" style="left:144px;right:0;top:0;bottom:9px"></div>
    <div class="foot"><span class="brand"><span class="dot"></span>Bright Towns Alliance</span><span class="num">5</span></div>
  </section>

  <section class="slide">
    <div style="padding-top:9px"><div class="h-slide">World Map</div><div class="rule"></div></div>
    <div class="photo" role="img" aria-label="World map with member city markers" style="left:16px;right:70px;top:28px;height:98px;background:linear-gradient(135deg,#c8cdd5,#a9b0bb);border-radius:4px"></div>
    <div style="position:absolute;right:10px;top:40px;width:54px;display:flex;flex-direction:column;gap:6px">
      <div style="display:flex;gap:3px;align-items:center;font-size:4.4px"><span style="width:6px;height:6px;background:var(--orange)"></span>Region A</div>
      <div style="display:flex;gap:3px;align-items:center;font-size:4.4px"><span style="width:6px;height:6px;background:var(--navy)"></span>Region B</div>
      <p class="txt">Members in over forty nations.</p>
    </div>
    <div class="foot"><span class="brand"><span class="dot"></span>Bright Towns Alliance</span><span class="num">6</span></div>
  </section>

  <!-- Row 5: timelines -->
  <section class="slide">
    <div style="padding-top:16px"><div class="h-slide">Start of The Timeline</div><div class="rule"></div></div>
    <div class="timeline"><div class="axis"><i style="width:20%"></i></div>
      <div class="stops">
        <div class="stop on"><div class="c">01</div><b>2016</b><p class="txt">Launch</p></div>
        <div class="stop"><div class="c">02</div><b>2017</b><p class="txt">Growth</p></div>
        <div class="stop"><div class="c">03</div><b>2018</b><p class="txt">Expand</p></div>
        <div class="stop"><div class="c">04</div><b>2019</b><p class="txt">Review</p></div>
        <div class="stop"><div class="c">05</div><b>2020</b><p class="txt">Future</p></div>
      </div></div>
    <div class="foot"><span class="brand"><span class="dot"></span>Bright Towns Alliance</span><span class="num">7</span></div>
  </section>

  <section class="slide">
    <div style="padding-top:16px"><div class="h-slide">Middle of The Timeline</div><div class="rule"></div></div>
    <div class="timeline"><div class="axis"><i style="width:50%"></i></div>
      <div class="stops">
        <div class="stop on"><div class="c">01</div><b>2016</b><p class="txt">Launch</p></div>
        <div class="stop on"><div class="c">02</div><b>2017</b><p class="txt">Growth</p></div>
        <div class="stop on"><div class="c">03</div><b>2018</b><p class="txt">Expand</p></div>
        <div class="stop"><div class="c">04</div><b>2019</b><p class="txt">Review</p></div>
        <div class="stop"><div class="c">05</div><b>2020</b><p class="txt">Future</p></div>
      </div></div>
    <div class="foot"><span class="brand"><span class="dot"></span>Bright Towns Alliance</span><span class="num">8</span></div>
  </section>

  <section class="slide">
    <div style="padding-top:16px"><div class="h-slide">End of The Timeline</div><div class="rule"></div></div>
    <div class="timeline"><div class="axis"><i style="width:100%"></i></div>
      <div class="stops">
        <div class="stop on"><div class="c">01</div><b>2016</b><p class="txt">Launch</p></div>
        <div class="stop on"><div class="c">02</div><b>2017</b><p class="txt">Growth</p></div>
        <div class="stop on"><div class="c">03</div><b>2018</b><p class="txt">Expand</p></div>
        <div class="stop on"><div class="c">04</div><b>2019</b><p class="txt">Review</p></div>
        <div class="stop on"><div class="c">05</div><b>2020</b><p class="txt">Future</p></div>
      </div></div>
    <div class="foot"><span class="brand"><span class="dot"></span>Bright Towns Alliance</span><span class="num">9</span></div>
  </section>

  <!-- Row 6: photo layouts -->
  <section class="slide">
    <div class="band-head">Bright Towns Alliance PowerPoint Template</div>
    <div class="cols" style="grid-template-columns:1fr 1fr">
      <div class="col"><div class="pic photo ph-tram" role="img" aria-label="Photograph of a city tram"></div><b>Transit</b><p class="txt">Short caption for this image.</p></div>
      <div class="col"><div class="pic photo ph-tram" role="img" aria-label="Photograph of a tram in a busy street"></div><b>Mobility</b><p class="txt">Short caption for this image.</p></div>
    </div>
    <div class="foot"><span class="brand"><span class="dot"></span>Bright Towns Alliance</span><span class="num">10</span></div>
  </section>

  <section class="slide">
    <div class="band-head">Bright Towns Alliance PowerPoint Template</div>
    <div class="cols" style="grid-template-columns:1fr 1fr 1fr">
      <div class="col"><div class="pic photo ph-street" role="img" aria-label="Photograph of tall city buildings"></div><b>Housing</b><p class="txt">Short caption here.</p></div>
      <div class="col"><div class="pic photo ph-city" role="img" aria-label="Photograph of a city avenue"></div><b>Streets</b><p class="txt">Short caption here.</p></div>
      <div class="col"><div class="pic photo ph-coast" role="img" aria-label="Photograph of a city square"></div><b>Public Space</b><p class="txt">Short caption here.</p></div>
    </div>
    <div class="foot"><span class="brand"><span class="dot"></span>Bright Towns Alliance</span><span class="num">11</span></div>
  </section>

  <section class="slide">
    <div class="band-head">Bright Towns Alliance PowerPoint Template</div>
    <div class="cols" style="grid-template-columns:1fr 1fr 1fr">
      <div class="col"><div class="pic photo ph-city" role="img" aria-label="Photograph of a modern station" style="height:54px"></div><div class="card-or"><b>Energy</b><p class="txt">Short caption.</p></div></div>
      <div class="col"><div class="pic photo ph-night" role="img" aria-label="Photograph of a city bridge at night" style="height:54px"></div><div class="card-or"><b>Water</b><p class="txt">Short caption.</p></div></div>
      <div class="col"><div class="pic photo ph-street" role="img" aria-label="Photograph of a shopping street" style="height:54px"></div><div class="card-or"><b>Waste</b><p class="txt">Short caption.</p></div></div>
    </div>
    <div class="foot"><span class="brand"><span class="dot"></span>Bright Towns Alliance</span><span class="num">12</span></div>
  </section>

  <!-- Row 7 -->
  <section class="slide">
    <div style="padding-top:14px"><div class="h-slide">Series Process</div><div class="rule"></div></div>
    <div class="process">
      <div class="chev">01</div><div class="chev alt">02</div><div class="chev">03</div><div class="chev alt">04</div>
    </div>
    <div class="proc-text">
      <div><b>Plan</b><p class="txt">Set clear goals.</p></div>
      <div><b>Build</b><p class="txt">Deliver the work.</p></div>
      <div><b>Measure</b><p class="txt">Track results.</p></div>
      <div><b>Share</b><p class="txt">Report findings.</p></div>
    </div>
    <div class="foot"><span class="brand"><span class="dot"></span>Bright Towns Alliance</span><span class="num">13</span></div>
  </section>

  <section class="slide">
    <div class="band-head">Bright Towns Alliance PowerPoint Template</div>
    <table class="data-table">
      <thead><tr><th>City</th><th>Transit</th><th>Energy</th><th>Water</th></tr></thead>
      <tbody>
        <tr><td>City One</td><td>82%</td><td>64%</td><td>71%</td></tr>
        <tr><td>City Two</td><td>75%</td><td>58%</td><td>66%</td></tr>
        <tr><td>City Three</td><td>69%</td><td>72%</td><td>80%</td></tr>
        <tr><td>City Four</td><td>88%</td><td>61%</td><td>59%</td></tr>
      </tbody>
    </table>
    <div class="foot"><span class="brand"><span class="dot"></span>Bright Towns Alliance</span><span class="num">14</span></div>
  </section>

  <section class="slide">
    <div class="photo ph-night" role="img" aria-label="City skyline at night photograph" style="inset:0"></div>
    <div class="contact-shade"></div>
    <div class="contact-left">
      <div class="brand light"><span class="dot"></span>Bright Towns Alliance</div>
      <h2>CONTACT US</h2>
    </div>
    <ul class="contact-list">
      <li><span class="ic"><svg width="7" height="7" viewBox="0 0 10 10" aria-hidden="true"><path d="M2 1l2 2-1 1.5a6 6 0 0 0 2.5 2.5L7 6l2 2-1.5 1.5C4 9 1 6 .5 2.5z" fill="#fff"/></svg></span>+1 555 014 2880</li>
      <li><span class="ic"><svg width="7" height="7" viewBox="0 0 10 10" aria-hidden="true"><rect x="1" y="2" width="8" height="6" fill="none" stroke="#fff"/><path d="M1 2l4 3.5L9 2" fill="none" stroke="#fff"/></svg></span>hello@brighttowns.example</li>
      <li><span class="ic"><svg width="7" height="7" viewBox="0 0 10 10" aria-hidden="true"><path d="M5 .5a3.5 3.5 0 0 0-3.5 3.5C1.5 7 5 9.5 5 9.5S8.5 7 8.5 4A3.5 3.5 0 0 0 5 .5z" fill="#fff"/><circle cx="5" cy="4" r="1.3" fill="#f4a321"/></svg></span>100 Civic Way, Springdale</li>
      <li><span class="ic"><svg width="7" height="7" viewBox="0 0 10 10" aria-hidden="true"><circle cx="5" cy="5" r="4" fill="none" stroke="#fff"/><path d="M1 5h8M5 1c-2 2.5-2 5.5 0 8M5 1c2 2.5 2 5.5 0 8" fill="none" stroke="#fff" stroke-width=".7"/></svg></span>www.brighttowns.example</li>
    </ul>
  </section>

</main>
</body>
</html>
```